依頼詳細
基礎化粧品シリーズのパッケージデザイン(外箱)
絵柄等はシリーズ全体で統一し、全体又はポイントで色味を変えて差別化したいと思っています。
化粧品本体のデザインは既に決定しており、容器は全体的にホワイトベースで、商品名の下にツノマタのワンポイントイラストが入ったシンプルなデザインになっています。(ワンポイントイラストのカラーは外箱デザイン決定後に、統一性のある色に決めようと思っています。)
中身がシンプルなので、外箱は目を引くようなデザインをと考えていますが、あまり派手すぎないものがいいです。
記載項目
W40×D32×H150mm
材質はまだ確定していません。
希望イメージ
シンプル 複雑
単色 カラフル
暗い 明るい
日常 高級
遊び心 厳粛
未来的 伝統的
女性的 男性的
希望する色
イメージしている色「海藻→青紫、赤紫系」「海、波→青緑系」
納品ファイル
• 高解像度JPG (.jpg)

```html
<!DOCTYPE html>
<html lang="en">
<head>
<meta charset="utf-8">
<title>Algue Claire – Cleansing Foam Carton</title>
<link rel="stylesheet" href="https://fonts.googleapis.com/css2?family=Cormorant+Garamond:wght@300;400;500&family=Noto+Serif+JP:wght@400&display=swap">
<style>
  :root {
    --page-light: #ececed;
    --page-dark: #bdbdc0;
    --sea-deep: #2f5fb8;
    --sea-mid: #5d8fd8;
    --sea-pale: #c9dcf3;
    --violet: #8f86c9;
    --rose: #c79ab7;
    --foam: #ffffff;
    --ink-soft: rgba(255,255,255,0.92);
  }
  * { margin: 0; padding: 0; box-sizing: border-box; }
  html, body { width: 878px; height: 1200px; overflow: hidden; }
  body {
    background: radial-gradient(ellipse at 50% 45%, var(--page-light) 0%, #dcdcde 55%, var(--page-dark) 100%);
    font-family: "Cormorant Garamond", serif;
    position: relative;
  }
  .carton-tab {
    position: absolute;
    left: 346px; top: 96px;
    width: 196px; height: 200px;
    background:
      linear-gradient(90deg, rgba(255,255,255,0) 0%, rgba(255,255,255,0.55) 40%, rgba(255,255,255,0.35) 70%, rgba(255,255,255,0) 100%),
      linear-gradient(180deg, var(--sea-pale) 0%, #9dbbe8 60%, var(--sea-mid) 100%);
  }
  .tab-emblem {
    position: absolute;
    left: 84px; top: 108px;
    width: 28px; height: 20px;
    background: var(--sea-deep);
    border-radius: 3px;
    opacity: 0.8;
  }
  .carton-front {
    position: absolute;
    left: 199px; top: 296px;
    width: 504px; height: 744px;
    overflow: hidden;
    background:
      radial-gradient(ellipse 60% 25% at 15% 88%, rgba(199,154,183,0.85) 0%, rgba(199,154,183,0) 100%),
      radial-gradient(ellipse 55% 30% at 85% 20%, rgba(143,134,201,0.55) 0%, rgba(143,134,201,0) 100%),
      radial-gradient(ellipse 70% 20% at 40% 55%, rgba(255,255,255,0.55) 0%, rgba(255,255,255,0) 100%),
      linear-gradient(170deg, #7fa6e2 0%, var(--sea-deep) 30%, var(--sea-mid) 52%, #3d6ec6 70%, var(--violet) 100%);
  }
  .light-band {
    position: absolute;
    left: 147px; top: 0;
    width: 196px; height: 100%;
    background: linear-gradient(90deg, rgba(255,255,255,0) 0%, rgba(255,255,255,0.45) 30%, rgba(255,255,255,0.3) 75%, rgba(255,255,255,0) 100%);
  }
  .band-edge {
    position: absolute; top: 0; height: 100%; width: 1px;
    background: rgba(255,255,255,0.6);
  }
  .band-edge.left { left: 147px; }
  .band-edge.right { left: 343px; }
  .band-text {
    position: absolute;
    left: 147px; width: 196px;
    text-align: center;
    color: var(--foam);
  }
  .brand-name {
    top: 46px;
    font-weight: 300;
    font-size: 40px;
    line-height: 1.0;
    letter-spacing: 3px;
  }
  .tagline {
    top: 136px;
    font-size: 12.5px;
    line-height: 1.35;
    color: var(--ink-soft);
  }
  .seaweed-motif {
    position: absolute;
    left: 220px; top: 276px;
    width: 50px; height: 46px;
    background: radial-gradient(circle, #ffffff 0%, rgba(255,255,255,0.75) 60%, rgba(255,255,255,0) 100%);
    border-radius: 6px;
  }
  .product-type {
    top: 466px;
    font-size: 17px;
    letter-spacing: 0.5px;
  }
  .product-type-jp {
    position: absolute;
    left: 203px; top: 496px;
    width: 84px; height: 22px;
    border: 1px solid var(--foam);
    text-align: center;
    font-family: "Noto Serif JP", serif;
    font-size: 11px;
    line-height: 20px;
    color: var(--foam);
    letter-spacing: 1px;
  }
  .maker {
    top: 548px;
    display: flex; flex-direction: column; align-items: center; gap: 4px;
  }
  .maker-dot {
    width: 10px; height: 10px; border-radius: 50%;
    background: var(--foam);
  }
  .maker-name {
    font-size: 9px; letter-spacing: 1.5px; color: var(--foam);
  }
</style>
</head>
<body>
  <div class="carton-tab">
    <div class="tab-emblem" role="img" aria-label="Small seaweed motif"></div>
  </div>
  <section class="carton-front">
    <div class="light-band"></div>
    <div class="band-edge left"></div>
    <div class="band-edge right"></div>
    <h1 class="band-text brand-name">ALGUE<br>CLAIRE</h1>
    <p class="band-text tagline">Beauty products from<br>seaweed "TSUNOMATA"<br>sea fiber, and minerals<br>drawn from the Ocean</p>
    <div class="seaweed-motif" role="img" aria-label="Seaweed illustration"></div>
    <p class="band-text product-type">Cleansing foam</p>
    <p class="product-type-jp">洗顔フォーム</p>
    <div class="band-text maker">
      <span class="maker-dot"></span>
      <span class="maker-name">MIRANE COSMETICS</span>
    </div>
  </section>
</body>
</html>
```